New business card for civil engineering company - "Keystone Audit"

We need a business card designed for our new structural engineering company.

The company name is "Keystone Audit" logo files attached.

We would like the following:
* Two-sided card
* Simple design

Information to be placed on the card:
Name - Marcus Dellow
Job Title - Director / Structural Engineer
Credentials - BEng(Hons), CPEng, CMengNZ, IntPE(NZ)
Email - marcus.dellow@keystoneaudit.co.nz
mobile - 0219364058
website - www.keystoneaudit.co.nz

```html
<!DOCTYPE html>
<html lang="en">
<head>
<meta charset="utf-8">
<title>Keystone Audit — Business Card</title>
<link href="https://fonts.googleapis.com/css2?family=Roboto:wght@400;500;700&display=swap" rel="stylesheet">
<style>
  :root {
    --page-bg: #e4e4e4;
    --card-white: #ffffff;
    --accent-blue: #4a8fd0;
    --deep-blue-top: #0c5782;
    --deep-blue-bottom: #063f6e;
    --ink: #3a3a3a;
    --tri-light: #a9c9e8;
    --tri-mid: #4f93cf;
    --tri-dark: #1c4f7d;
  }
  * { box-sizing: border-box; margin: 0; padding: 0; }
  html, body {
    width: 1200px; height: 1200px; overflow: hidden;
    background: var(--page-bg);
    font-family: "Roboto", Arial, sans-serif;
  }
  .canvas { position: relative; width: 1200px; height: 1200px; }
  .card {
    position: absolute; left: 262px; width: 686px; height: 392px; overflow: hidden;
  }
  .card--front { top: 165px; background: var(--card-white); }
  .card--back {
    top: 653px;
    background: linear-gradient(180deg, var(--deep-blue-top), var(--deep-blue-bottom));
  }

  .corner-pattern { position: absolute; }
  .corner-pattern--top {
    left: 0; top: 0; width: 270px; height: 145px;
    background: linear-gradient(135deg, var(--tri-dark) 0%, var(--tri-mid) 40%, var(--tri-light) 75%, rgba(255,255,255,0) 100%);
    clip-path: polygon(0 0, 100% 0, 0 100%);
  }
  .corner-pattern--bottom {
    right: 0; bottom: 0; width: 250px; height: 142px;
    background: linear-gradient(315deg, var(--tri-dark) 0%, var(--tri-mid) 40%, var(--tri-light) 75%, rgba(255,255,255,0) 100%);
    clip-path: polygon(100% 0, 100% 100%, 0 100%);
  }

  .identity {
    position: absolute; right: 42px; top: 39px; text-align: right;
  }
  .identity__name {
    font-size: 23px; font-weight: 500; color: var(--accent-blue); line-height: 1.1;
  }
  .identity__credentials {
    font-size: 14px; color: var(--accent-blue); margin-top: 2px;
  }
  .identity__role {
    font-size: 15.5px; color: var(--ink); margin-top: 4px;
  }

  .contact {
    position: absolute; left: 40px; top: 300px; list-style: none;
  }
  .contact__item {
    display: flex; align-items: center; gap: 9px;
    font-size: 15px; color: var(--ink); line-height: 20px;
  }
  .contact__icon { width: 13px; height: 13px; flex: none; }

  .brand {
    position: absolute; left: 0; right: 0; top: 274px; text-align: center; color: #fff;
  }
  .brand__name {
    font-size: 28px; font-weight: 400; letter-spacing: 4px; line-height: 1;
  }
  .brand__tagline {
    font-size: 11.5px; letter-spacing: 3.4px; margin-top: 12px;
  }
</style>
</head>
<body>
<main class="canvas">
  <section class="card card--front">
    <div class="corner-pattern corner-pattern--top" role="img" aria-label="Scattered blue triangle pattern"></div>
    <div class="corner-pattern corner-pattern--bottom" role="img" aria-label="Scattered blue triangle pattern"></div>

    <div class="identity">
      <p class="identity__name">Marcus Dellow BEng</p>
      <p class="identity__credentials">(Hons), CPEng, CMengNZ, IntPE(NZ)</p>
      <p class="identity__role">Director / Structural Engineer</p>
    </div>

    <ul class="contact">
      <li class="contact__item">
        <svg class="contact__icon" viewBox="0 0 16 16"><path fill="#4a8fd0" d="M3.5 1l2.5 3-1.5 1.8c.8 1.8 2.2 3.3 4 4.2L10.3 8.5l3.2 2.4-1.2 3C7 14 2 9 1.5 3.3z"/></svg>
        <span>0219364058</span>
      </li>
      <li class="contact__item">
        <svg class="contact__icon" viewBox="0 0 16 16"><rect x="1" y="3" width="14" height="10" fill="#4a8fd0"/><path d="M1 3.5l7 5 7-5" stroke="#fff" stroke-width="1.3" fill="none"/></svg>
        <span>marcus.dellow@keystoneaudit.co.nz</span>
      </li>
      <li class="contact__item">
        <svg class="contact__icon" viewBox="0 0 16 16"><circle cx="8" cy="8" r="7" fill="#4a8fd0"/><path d="M4 5c2 0 2 2 4 2s1 3 3 3M9 2c-1 2 1 3 0 4" stroke="#fff" stroke-width="1.2" fill="none"/></svg>
        <span>www.keystoneaudit.co.nz</span>
      </li>
    </ul>
  </section>

  <section class="card card--back">
    <div class="brand">
      <p class="brand__name">KEYSTONE AUDIT</p>
      <p class="brand__tagline">PEER REVIEW SPECIALISTS</p>
    </div>
  </section>
</main>
</body>
</html>
```